VELOTRAK End User Instruction Guide

I need to create a 5 to 7-page instruction guides for customers who purchased a phone system from our company. The document is a quick reference guide that will help end-users learn how to set up and use their new desk phone and software applications. I need the guide to be 3 x 5 or 6 x 8 in size and will fold like a book.

Target Market(s)

Business users / Brontel Desk Phone Users / VeLOTRAK Portal users

Industry/Entity Type

Telecommunications

Font styles to use
Serif

Colors
0758a5
ffffff

Requirements
Must have
• Need to have step-by-step instructions that include the information from the QuickStart guide I provided. I need to see an image of the phone with an arrow pointing to the key on the phone that should be pressed. For example, when checking voicemail the Messages key is pressed and I want to highlight this button or call it out somehow.

I need to have three pages for setup instructions, one page for shortcuts or features codes and our support contacts on the last page.
Nice to have
• I want to have a page for notes that the end-user can use during training. I would also like to have a blank space next to passwords and user ID's so they can be filled out with specific details that are provided during their training. For example, in the voicemail section, I include a default PIN. I would like to leave this blank and let the end-user fill it out during training.
Should not have
• Complex shapes and designs. I like straight lines and a simple easy to understand layout.

```html
<!DOCTYPE html>
<html lang="en">
<head>
<meta charset="utf-8">
<title>VELOTRAK End User Quick Start Guide</title>
<link rel="stylesheet" href="https://fonts.googleapis.com/css2?family=Open+Sans:wght@400;600;700&family=Oswald:wght@500&display=swap">
<style>
:root{
  --stage:#363636;
  --paper:#ffffff;
  --paper-shade:#eeeeef;
  --ink:#2a2a2a;
  --navy:#1d3b7c;
  --brand:#2b3952;
  --step:#3c4350;
  --muted:#8a8f98;
}
*{box-sizing:border-box;margin:0;padding:0}
html,body{width:1200px;height:1200px;overflow:hidden;background:var(--stage)}
body{position:relative;font-family:"Open Sans",Arial,sans-serif;color:var(--ink)}
.spread{position:absolute;width:512px;height:307px;display:flex;background:var(--paper)}
.spread-a{left:60px;top:286px}
.spread-b{left:622px;top:286px}
.spread-c{left:60px;top:629px;height:306px}
.spread-d{left:622px;top:629px;height:306px}
.page{position:relative;width:256px;height:100%;padding:14px 14px 0 18px;font-size:7.3px;line-height:1.4;overflow:hidden}
.page-shaded{background:linear-gradient(180deg,var(--paper-shade),var(--paper) 45%,var(--paper-shade))}
.page-left-shade{background:linear-gradient(90deg,var(--paper),var(--paper-shade))}
.texture{position:absolute;left:0;right:0;bottom:0;height:90px;background:linear-gradient(0deg,rgba(150,150,160,.18),rgba(150,150,160,0))}
.folio{position:absolute;bottom:8px;font-size:6.5px;color:var(--ink)}
.folio-l{right:14px}.folio-r{right:18px}
.wordmark{font-weight:700;color:var(--brand);letter-spacing:.5px;display:flex;align-items:center;gap:5px}
.wordmark .mark{width:10px;height:10px;background:var(--brand)}
h1.guide-title{font-size:12.5px;color:var(--navy);font-weight:600;text-align:center}
.cover-title{font-family:"Oswald",sans-serif;font-size:14px;color:var(--navy);text-align:center;padding-bottom:6px;border-bottom:1px solid var(--brand);width:168px;margin:0 auto}
h2{font-size:8.8px;color:var(--navy);font-weight:600;margin:6px 0 4px}
h3{font-size:8px;font-weight:400;margin:6px 0 3px}
.step{display:flex;align-items:center;gap:4px;font-size:8.8px;color:var(--navy);font-weight:600;margin:8px 0 6px}
.step b{background:var(--step);color:#fff;padding:1px 3px;font-weight:600}
ol,ul{padding-left:11px}
li{margin-bottom:2px}
.arrow::before{content:"➤ ";color:var(--step)}
.blue{color:var(--navy);font-weight:600}
.contact{font-size:6.4px;margin-top:6px;display:flex;gap:5px;align-items:flex-start}
.contact svg{flex:none;margin-top:1px}
.shot{border:1px solid #777;background:linear-gradient(180deg,#e4e6ea,#f7f7f8)}
.tiny{font-size:5.5px;line-height:1.3}
.tiny h2{font-size:9.5px;margin:3px 0 2px}
.tiny h4{font-size:6.4px;font-weight:700;margin:2px 0}
.cols{display:flex;gap:8px}
</style>
</head>
<body>

<!-- Spread 1: back cover + front cover -->
<section class="spread spread-a">
  <div class="page">
    <div class="texture" role="img" aria-label="Faint grey network line pattern"></div>
    <div style="margin-top:96px" class="wordmark"><span class="mark"></span><span style="font-size:12px">VELOTRAK</span></div>
    <div class="contact"><svg width="6" height="7" viewBox="0 0 6 7"><path d="M3 0a2.5 2.5 0 0 1 2.5 2.5C5.5 4.5 3 7 3 7S.5 4.5.5 2.5A2.5 2.5 0 0 1 3 0z" fill="#2b3952"/></svg><span>1820 Harbor Ln Suite C<br>Lakemont, Ohio 44012<br>United States</span></div>
    <div class="contact" style="margin-top:8px"><svg width="6" height="6" viewBox="0 0 6 6"><path d="M1 .5l1 1.3-.6.8a4 4 0 0 0 2 2l.8-.6 1.3 1-.6.8C2.5 5.5.5 3.5.2 1.2z" fill="#555"/></svg><span>(555) 014-2290</span></div>
    <div class="contact" style="margin-top:6px"><svg width="6" height="6" viewBox="0 0 6 6"><circle cx="3" cy="3" r="2.6" fill="#555"/></svg><span>velotrakcomms.example</span></div>
  </div>
  <div class="page page-shaded">
    <div class="texture" role="img" aria-label="Faint grey network line pattern"></div>
    <div class="wordmark" style="justify-content:center;margin-top:94px"><span class="mark" style="width:14px;height:14px"></span><span style="font-size:17px">VELOTRAK</span></div>
    <div class="cover-title" style="margin-top:18px">END USER QUICK START GUIDE</div>
  </div>
</section>

<!-- Spread 2: pages 2-3 -->
<section class="spread spread-b">
  <div class="page page-left-shade">
    <h1 class="guide-title" style="margin-top:10px">End User Quick Start Guide</h1>
    <svg width="228" height="6" viewBox="0 0 228 6" style="display:block;margin:2px auto 0"><circle cx="112" cy="3" r="2.2" fill="#2b3952"/></svg>
    <div class="step"><b>Step 1:</b> Create your personal voicemail greeting</div>
    <h3 style="font-size:8.4px">Accessing Voicemail from your desk phone</h3>
    <div class="arrow" style="font-size:7.8px;margin-top:6px">To access voicemail</div>
    <ol>
      <li>Press the <span class="blue">Messages</span> button on your phone to access your voicemail box, or dial 5001 if you can not identify the voicemail button.</li>
      <li>If you subscribe to multiple mailboxes, a list of mailboxes may appear. Select the mail box you want to access.</li>
      <li>When prompted, enter your default voicemail pin ______, and then press #.</li>
    </ol>
    <div class="arrow" style="margin-top:3px">To access another person's mailbox</div>
    <ol>
      <li>Dial <b>5000</b>.</li>
      <li>When prompted, enter the other person's extension number.</li>
      <li>Enter the voicemail PIN of the other person's mailbox, followed by #.</li>
    </ol>
    <span class="folio folio-l">2</span>
  </div>
  <div class="page page-shaded">
    <div class="texture" role="img" aria-label="Faint grey network line pattern"></div>
    <h2 style="margin-top:8px">Setting Up Your Mailbox</h2>
    <p>The first time you log in to your mailbox you are walked through recording your name for the directory and recording your personal greeting. The name recording is for the dial-by-name directory, so when someone enters the first three letters of your last name, it will play back your name recording.</p>
    <p style="margin-top:6px">The greeting plays when your mailbox is reached. It is very important to make a custom message, as many callers will not leave messages at mailboxes that have generic greetings.</p>
    <div class="wordmark" style="justify-content:center;margin-top:78px"><span class="mark"></span><span style="font-size:13px">VELOTRAK</span></div>
    <span class="folio folio-r">3</span>
  </div>
</section>

<!-- Spread 3: pages 4-5 -->
<section class="spread spread-c">
  <div class="page page-left-shade">
    <div class="wordmark" style="justify-content:center;margin-top:10px"><span class="mark"></span><span style="font-size:13px">VELOTRAK</span></div>
    <h2 style="margin-top:14px;font-weight:400">Accessing Voicemail from the user portal</h2>
    <div class="arrow" style="font-size:8px;margin-top:6px">To access the web portal</div>
    <ol start="2"><li>Start a web browser.</li><li>Go to phone.velotrakcomms.example</li></ol>
    <ul style="font-size:6.3px;margin-top:6px">
      <li>Click in the <b>Login</b> name field and type ext@customerdomain. Your customerdomain typically is the same as your email address domain.</li>
      <li style="margin-top:6px">Click in the <b>Password</b> field and enter your user password. (default password is ______)</li>
    </ul>
    <div class="shot" role="img" aria-label="Screenshot of the portal login form with name and password fields" style="width:88px;height:72px;margin:14px 0 0 64px"></div>
    <span class="folio" style="left:240px">4</span>
  </div>
  <div class="page page-shaded">
    <h2 style="margin-top:8px;font-size:10px;font-weight:400">VOICEMAIL</h2>
    <p>You configure voicemail using the Messages Page. This page has two tabs for handling voicemail.</p>
    <ul style="margin-top:3px"><li><b>Messages</b> - see "Messages" below.</li><li><b>Settings</b> - see "Settings" on the next page.</li></ul>
    <p style="margin-top:3px">To display the Messages page, click the <b>Messages</b> icon at the top of the page :</p>
    <div class="shot" role="img" aria-label="Screenshot of the portal Messages page with toolbar icons and message list" style="width:192px;height:86px;margin:8px 0 0 22px"></div>
    <div class="arrow" style="margin-top:8px">To record a greeting</div>
    <ol start="4" style="font-size:6.4px"><li>From the <b>Settings</b> tab of the Messages page, click the speaker icon</li><li>Next to <b>New Greeting</b>, click <b>Record</b> and the system will call you, or upload an existing greeting.</li></ol>
    <span class="folio folio-r">5</span>
  </div>
</section>

<!-- Spread 4: pages 8-9 -->
<section class="spread spread-d">
  <div class="page page-left-shade" style="font-size:6.2px">
    <div class="wordmark" style="justify-content:center;margin-top:2px"><span class="mark"></span><span style="font-size:13px">VELOTRAK</span></div>
    <div class="step" style="margin:6px 0 2px"><b>Step 2:</b> Using your desk phone</div>
    <div class="arrow blue" style="font-size:8.5px;font-weight:400">Making Calls</div>
    <p>Making a call with your phone does not require a leading 9. You can dial on-hook or off-hook.</p>
    <div class="blue" style="font-weight:400;font-size:7.4px;margin-top:3px">To dial on-hook</div>
    <ul><li>Dial the phone number.</li><li>Pick up the handset, headset, or speaker.</li></ul>
    <div class="blue" style="font-weight:400;font-size:7.4px">To dial off-hook</div>
    <p>Pick up the handset, headset, or speaker.<br><b>Dial the phone number.</b><br>Calls to the US and Canada are all dialed using 10 or 11 digits.</p>
    <div class="blue" style="font-size:7.4px;margin-top:3px">Receiving Calls</div>
    <p>When a call comes in, you can answer it via a headset, speaker phone, or handset.</p>
    <div class="cols" style="margin-top:3px"><div style="width:110px">To answer a call using a handset<br>&nbsp; ✔ Lift the handset off-hook.</div><div>To answer a call using a speakerphone<br>✔ Press the Speaker button.</div></div>
    <div class="blue" style="font-weight:400;margin-top:4px">To answer a call using a headset</div>
    <p>Usage depends on how the headset is connected. Often, you'll press the button on the headset or press the headset button on the phone.</p>
    <span class="folio folio-l">8</span>
  </div>
  <div class="page page-shaded tiny">
    <h2 style="font-size:11px;margin-top:0">Handling Calls</h2>
    <p>Your cloud PBX features various ways to move calls around, including attended transfer, unattended (blind) transfer, voicemail transfer, park, and more. In this section, references to BLFs are the 1-touch buttons to extensions common at front-desk phones.</p>
    <h2>Attended Transfer</h2>
    <p>Attended transfer allows you to speak to the transfer recipient prior to completing the transfer while the caller is on hold.</p>
    <div class="arrow" style="font-size:6.4px">To perform an attended transfer using Quorvex and Brontel phones</div>
    <ol start="6"><li>Press the <b>Transfer</b> key/softkey on your phone.</li><li>Dial the recipient's extension or press their BLF.</li><li>Speak to the recipient, and then either press <b>Transfer</b> again to complete or cancel if the recipient cannot take the call.</li></ol>
    <h2>Blind Transfer</h2>
    <div class="arrow" style="font-size:6.4px;font-weight:700">To blind transfer using Brontel phones</div>
    <ol start="9"><li><b>Press Transfer.</b></li><li>Dial the extension of the recipient. Press Transfer</li></ol>
    <h2>Transfers to External Numbers</h2>
    <p>A transfer can also go to an external number such as a cell phone. Follow the transfer directions above but instead of dialing an extension, dial a 10 digit phone number.</p>
    <h2>Park and Hold</h2>
    <p>On your phone system, hold is a local function. This means a call held on your phone cannot be picked up at another station. Park is a system-wide function. This means a call parked at one phone may be picked up by any phone.</p>
    <div class="arrow" style="font-size:6.4px;font-weight:700">To park a call</div>
    <ol start="11"><li>Dial *** in an active call from any phone. The system says, "The call is parked at 7xx."</li><li>Hang up. To retrieve the parked call, dial <b>7xx</b> where <b>xx</b> is the number stated by the system.</li></ol>
    <span class="folio folio-r">9</span>
  </div>
</section>

</body>
</html>
```